Business card design for upmarket Home Technology design and Installation company

Hello designers, we need a great business card designed.
We need it to convey high tech, and also sophistication .
We work with some of the most affluent people in the world building them home technology systems, and A/V entertainment systems.

Services offered include the following:
Design, sales, installation, and maintenance of

*Home Automation systems
*Distributed / Multi-Room Audio and Video
*High Performance Networks & WiFi
* Lighting and Shade Control
*Home cinema
*Security and CCTV Systems

I have included a copy of our logo to use for your design efforts.

Target Market(s)

Upmarket clients with multi million euro villas.

Industry/Entity Type

Home technology

Contact Information for Business Card

NAME: Derek Halvin ADDRESS: Carrer Bellamar Local 42, Cala Torrent, 07293 PHONE: +34-652-918-204 EMAIL: DHalvin@VORTELhomesystems.example WEB: www.vortelhomesystems.example

Requirements
Must have
• Our Logo, and our tagline

```html
<!DOCTYPE html>
<html lang="en">
<head>
<meta charset="utf-8">
<title>VORTEL Business Card</title>
<link rel="stylesheet" href="https://fonts.googleapis.com/css2?family=Dosis:wght@500;600&family=Nunito:wght@600;700&display=swap">
<style>
  :root {
    --backdrop: #d0d0d0;
    --card: #242424;
    --card-deep: #151515;
    --card-soft: #3a3a3a;
    --gold: #d9ae5a;
    --white: #ffffff;
    --muted: #b4b4b4;
    --glow: #2e2e2e;
  }
  * { margin: 0; padding: 0; box-sizing: border-box; }
  html, body { width: 1200px; height: 1000px; overflow: hidden; }
  body { background: var(--backdrop); position: relative; font-family: "Nunito", sans-serif; }

  .card {
    position: absolute;
    left: 293px;
    width: 613px;
    height: 352px;
    border-radius: 28px;
    background: var(--card);
    overflow: hidden;
    box-shadow: 0 22px 40px rgba(0,0,0,0.35);
  }
  .card--front { top: 92px; }
  .card--back { top: 499px; }

  .front-decor {
    position: absolute;
    left: 290px;
    top: 0;
    width: 323px;
    height: 352px;
    background: radial-gradient(circle at 60% 62%, var(--card) 0 32%, var(--glow) 34% 56%, var(--card) 60%);
  }

  .brand-name {
    font-family: "Dosis", sans-serif;
    font-weight: 600;
    color: var(--gold);
    letter-spacing: 6px;
    line-height: 1;
  }
  .brand-tagline {
    font-family: "Dosis", sans-serif;
    font-weight: 600;
    color: var(--gold);
    letter-spacing: 1px;
    line-height: 1;
  }

  .front-brand { position: absolute; left: 46px; top: 42px; }
  .front-brand .brand-name { font-size: 42px; }
  .front-brand .brand-tagline { font-size: 16px; margin: 6px 0 0 19px; }

  .person-name {
    position: absolute;
    left: 48px; top: 136px;
    font-family: "Dosis", sans-serif;
    font-weight: 500;
    font-size: 31px;
    letter-spacing: 2px;
    color: var(--white);
  }
  .address {
    position: absolute;
    left: 48px; top: 186px;
    font-size: 12.5px;
    line-height: 16px;
    letter-spacing: 2px;
    color: var(--muted);
    font-weight: 600;
    font-style: normal;
  }
  .contacts {
    position: absolute;
    left: 47px; top: 245px;
    list-style: none;
  }
  .contacts li {
    display: flex;
    align-items: center;
    height: 21px;
    font-size: 14.5px;
    letter-spacing: 2.4px;
    color: var(--white);
    font-weight: 600;
  }
  .contacts svg { width: 14px; height: 14px; margin-right: 8px; fill: var(--gold); flex: none; }

  .back-pattern {
    position: absolute; inset: 0;
    background: linear-gradient(90deg, var(--card-deep) 0%, #202020 50%, var(--card-soft) 100%);
  }
  .back-brand {
    position: absolute;
    left: 276px; top: 209px;
    display: flex;
    align-items: center;
    gap: 14px;
  }
  .back-brand .mark {
    width: 56px; height: 56px; border-radius: 50%;
    background: var(--gold);
  }
  .back-brand .brand-name { font-size: 40px; }
  .back-brand .brand-tagline { font-size: 17px; text-align: center; margin-top: 6px; }
</style>
</head>
<body>
  <section class="card card--front">
    <div class="front-decor" role="img" aria-label="Large faint brand symbol decoration on the right side of the card"></div>
    <div class="front-brand">
      <div class="brand-name">VORTEL</div>
      <div class="brand-tagline">HOME SYSTEMS</div>
    </div>
    <h1 class="person-name">DEREK HALVIN</h1>
    <address class="address">CARRER BELLAMAR LOCAL 42,<br>CALA TORRENT, 07293</address>
    <ul class="contacts">
      <li><svg viewBox="0 0 24 24"><path d="M6.6 10.8a15.1 15.1 0 0 0 6.6 6.6l2.2-2.2c.3-.3.7-.4 1-.2 1.1.4 2.3.6 3.6.6.6 0 1 .4 1 1V20c0 .6-.4 1-1 1A17 17 0 0 1 3 4c0-.6.4-1 1-1h3.5c.6 0 1 .4 1 1 0 1.3.2 2.5.6 3.6.1.3 0 .7-.2 1z"/></svg>+34-652-918-204</li>
      <li><svg viewBox="0 0 24 24"><path d="M2 5h20v14H2z M2 5l10 8 10-8" fill="none" stroke="#d9ae5a" stroke-width="2.5"/></svg>DHALVIN@VORTELHOMESYSTEMS.EXAMPLE</li>
      <li><svg viewBox="0 0 24 24"><circle cx="12" cy="12" r="9" fill="none" stroke="#d9ae5a" stroke-width="2"/><path d="M3 12h18M12 3c3 3 3 15 0 18M12 3c-3 3-3 15 0 18M5 7.5h14M5 16.5h14" fill="none" stroke="#d9ae5a" stroke-width="1.6"/></svg>VORTELHOMESYSTEMS.EXAMPLE</li>
    </ul>
  </section>

  <section class="card card--back">
    <div class="back-pattern" role="img" aria-label="Embossed repeating pattern of brand symbols across the card, dark on the left fading lighter to the right"></div>
    <div class="back-brand">
      <div class="mark" aria-hidden="true"></div>
      <div>
        <div class="brand-name">VORTEL</div>
        <div class="brand-tagline">HOME SYSTEMS</div>
      </div>
    </div>
  </section>
</body>
</html>
```